" Window Blinds and Shutters Business Card Design"

We require a business card design for a new windows blinds and shutters company based in Sydney.
The business name is 'Harbourlight Blinds and Shutters'.
We supply and install homes and businesses with internal and external window furnishings and finishes. This includes varieties of window blinds and window shutters.

Benefits of Harbourlight Blinds and Shutters :
Added security and privacy,
The ability to control the amount of sunlight,
Regulate internal temperature.

Blinds varieties:
Roller Blinds, Double Roller Blinds, Roman Blinds, Vertical Blinds, Aluminium venetians, Timber venetians and PVC Venetians.

Shutters varieties:
Plantation Shutters, Aluminium Louvre Shutters, Roller Shutters and Security Shutters .

Hi Designers,

Please have a look at my Business card design brief. I need your help to start my new business.

Thanks,

Daniel.

Reason: not 100% happy with the options available, close to 90% happy, need a little more refinement. Thank You & Good Luck

Target Market(s)

Home owners, business owners, shift workers , and new home builders.

Industry/Entity Type

Security

Contact Information for Business Card

Harbourlight Blinds and Shutters,

Daniel Brostow mobile: 0417586204,
Corey Wendt mobile: 0419248653,

email: daniel.brostow@mailvista.net
web: harbourlightblindsandshutters.com.au

Colors
ffffff
9d9d9d
f78f20

Requirements
Must have
• ON FRONT OF CARD
I have attached a picture of logo and need a designer to design a font logo for Harbourlight Blinds and Shutters similar, or open to suggestions.

FRONT OF CARD
Company message/:
"Safeguarding windows by design"

BACK OF CARD
'For a FREE measure & quote call Daniel - 0417586204"
Nice to have
• Elegant yet professional.

Soft colours appealing to both male & female clients.

Should not have

• Unprofessional fonts

```html
<!DOCTYPE html>
<html lang="en">
<head>
<meta charset="utf-8">
<title>Harbourlight Blinds and Shutters – Business Card</title>
<link rel="stylesheet" href="https://fonts.googleapis.com/css2?family=Michroma&family=Open+Sans:wght@400;600&display=swap">
<style>
  :root {
    --white: #ffffff;
    --grey: #9d9d9d;
    --grey-light: #c4c4c4;
    --orange: #f78f20;
    --orange-deep: #f26a1b;
    --red: #e8322a;
    --yellow: #ffd84a;
    --stage: #ece8e3;
  }
  * { margin: 0; padding: 0; box-sizing: border-box; }
  html, body { width: 1200px; height: 784px; overflow: hidden; }
  body {
    background: var(--stage);
    display: flex;
    align-items: center;
    justify-content: center;
    gap: 40px;
    font-family: "Open Sans", Arial, sans-serif;
  }
  .card {
    position: relative;
    width: 550px;
    height: 314px;
    overflow: hidden;
    box-shadow: 0 6px 18px rgba(0,0,0,0.18);
  }

  /* Back of card */
  .card-back {
    background: linear-gradient(180deg, var(--orange) 0%, var(--orange-deep) 45%, var(--red) 100%);
    color: var(--white);
  }
  .varieties {
    position: absolute;
    top: 20px;
    left: 0;
    right: 0;
    text-align: center;
    font-family: "Michroma", "Arial Narrow", sans-serif;
    font-size: 9px;
    line-height: 14px;
    letter-spacing: 0.06em;
    text-transform: uppercase;
  }
  .varieties h2 {
    font-size: 9px;
    font-weight: 400;
    color: var(--yellow);
  }
  .varieties ul { list-style: none; }
  .varieties .group + .group { margin-top: 10px; }
  .back-brand {
    position: absolute;
    right: 24px;
    top: 200px;
    font-family: "Michroma", "Arial Narrow", sans-serif;
    color: var(--white);
    text-transform: uppercase;
    text-align: center;
  }
  .back-brand .brand-main {
    display: block;
    font-size: 20px;
    line-height: 24px;
  }
  .back-brand .brand-sub {
    display: block;
    font-size: 7px;
    line-height: 10px;
    letter-spacing: 0.3em;
  }
  .quote-call {
    position: absolute;
    left: 26px;
    bottom: 24px;
    font-size: 17px;
    line-height: 24px;
    color: var(--yellow);
  }

  /* Front of card */
  .card-front { background: var(--white); }
  .front-brand {
    position: absolute;
    top: 44px;
    left: 0;
    right: 0;
    text-align: center;
    font-family: "Michroma", "Arial Narrow", sans-serif;
    font-size: 38px;
    line-height: 46px;
    color: var(--orange);
    text-transform: uppercase;
  }
  .front-brand .brand-sub {
    display: block;
    font-size: 16px;
    line-height: 24px;
    letter-spacing: 0.28em;
  }
  .tagline-band {
    position: absolute;
    top: 150px;
    left: 0;
    right: 0;
    height: 18px;
    background: linear-gradient(90deg, var(--grey) 0%, var(--grey-light) 100%);
    font-family: "Michroma", "Arial Narrow", sans-serif;
    font-size: 10px;
    line-height: 18px;
    letter-spacing: 0.55em;
    color: var(--white);
    text-transform: uppercase;
    padding-left: 20px;
    white-space: nowrap;
  }
  .contact-panel {
    position: absolute;
    top: 168px;
    left: 0;
    right: 0;
    bottom: 0;
    background: linear-gradient(180deg, var(--orange) 0%, var(--orange-deep) 100%);
    padding: 10px 24px;
    color: var(--white);
    font-size: 15px;
    line-height: 19px;
  }
  .contact-name { color: var(--yellow); }
  .contact-line { display: flex; align-items: center; gap: 8px; }
  .contact-line svg { width: 14px; height: 14px; flex: none; }
  .contact-web { margin-top: 8px; }
</style>
</head>
<body>

  <section class="card card-back" aria-label="Back of business card">
    <div class="varieties">
      <div class="group">
        <h2>Blinds Varieties</h2>
        <ul>
          <li>Roller Blinds</li>
          <li>Double Roller Blinds</li>
          <li>Roman Blinds</li>
          <li>Vertical Blinds</li>
          <li>Aluminium Venetians</li>
          <li>Timber Venetians and PVC Venetians</li>
        </ul>
      </div>
      <div class="group">
        <h2>Shutters Varieties</h2>
        <ul>
          <li>Plantation Shutters</li>
          <li>Aluminium Louvre Shutters</li>
          <li>Roller Shutters and Security Shutters</li>
        </ul>
      </div>
    </div>
    <p class="back-brand"><span class="brand-main">Harbourlight</span><span class="brand-sub">Blinds and Shutters</span></p>
    <p class="quote-call">For a FREE measure &amp; quote<br>call Daniel - 0417586204</p>
  </section>

  <section class="card card-front" aria-label="Front of business card">
    <h1 class="front-brand">Harbourlight<span class="brand-sub">Blinds and Shutters</span></h1>
    <p class="tagline-band">Safeguarding windows by design</p>
    <div class="contact-panel">
      <p class="contact-name">Daniel Brostow</p>
      <p class="contact-line">
        <svg viewBox="0 0 16 16" aria-hidden="true"><path fill="var(--red)" d="M3.5 1l2.5 3-1.5 2c1 2 2.5 3.5 4.5 4.5l2-1.5 3 2.5-1.5 2.5C7 14 2 9 1 2.5z"/></svg>
        0417586204
      </p>
      <p class="contact-name">Corey Wendt</p>
      <p class="contact-line">
        <svg viewBox="0 0 16 16" aria-hidden="true"><path fill="var(--red)" d="M3.5 1l2.5 3-1.5 2c1 2 2.5 3.5 4.5 4.5l2-1.5 3 2.5-1.5 2.5C7 14 2 9 1 2.5z"/></svg>
        0419248653
      </p>
      <p class="contact-line contact-web">
        <svg viewBox="0 0 16 16" aria-hidden="true"><rect x="1.5" y="3.5" width="13" height="9" fill="none" stroke="var(--red)" stroke-width="1.6"/><path d="M1.5 3.5l6.5 5 6.5-5" fill="none" stroke="var(--red)" stroke-width="1.6"/></svg>
        daniel.brostow@mailvista.net
      </p>
      <p class="contact-line">
        <svg viewBox="0 0 16 16" aria-hidden="true"><g fill="none" stroke="var(--red)" stroke-width="1.4"><circle cx="8" cy="8" r="6.5"/><ellipse cx="8" cy="8" rx="3" ry="6.5"/><path d="M1.5 8h13"/></g></svg>
        harbourlightblindsandshutters.com.au
      </p>
    </div>
  </section>

</body>
</html>
```